Tidewell Electrical Solutions

On one side. LOGO (underneath:) Commercial Industrial Residential

- NAME & CONTACT DETAILS

Martin K. Oduya
Project Manager

(Cell icon) (441) 555-0187
(Email icon) twlelectricalsoultions@mailpost-demo.com
(Facebook & Instagram icons )@twlelectricalsolutions

Other side: LOGO - underneath ELECTRICAL CONSTRUCTION & MAINTENANCE . LED LIGHTING & AUTOMATION . LIFE SAFETY SYSTEMS (FIRE ALARM / SECURITY) . DATA & COMMUNICATION

```html
<!DOCTYPE html>
<html lang="en">
<head>
<meta charset="utf-8">
<title>Tidewell Electrical Solutions – Business Card</title>
<link rel="stylesheet" href="https://fonts.googleapis.com/css2?family=Montserrat:wght@500&family=Roboto:wght@400;500&display=swap">
<style>
  :root {
    --teal: #10566c;
    --ink: #3b3b3c;
    --dark: #262a2c;
    --faint: #ececec;
    --paper: #ffffff;
    --backdrop: #e4e4e4;
  }
  * { box-sizing: border-box; margin: 0; padding: 0; }
  html, body { width: 1200px; height: 965px; overflow: hidden; }
  body {
    background: var(--backdrop);
    font-family: "Roboto", Arial, sans-serif;
    position: relative;
  }
  .card {
    position: absolute;
    left: 278px;
    width: 647px;
    height: 369px;
    overflow: hidden;
  }
  .card--front { top: 97px; background: var(--paper); }
  .card--back { top: 503px; background: var(--teal); }

  .brand {
    position: absolute;
    display: flex;
    align-items: center;
    gap: 14px;
    font-family: "Montserrat", Arial, sans-serif;
    font-weight: 500;
    text-transform: uppercase;
    letter-spacing: 0.14em;
    line-height: 1.12;
  }
  .brand__mark { width: 18px; height: 18px; flex: none; }
  .card--front .brand { left: 23px; top: 36px; font-size: 22px; color: var(--teal); }
  .card--front .brand__mark { background: var(--teal); }
  .card--back .brand { left: 94px; top: 128px; font-size: 30px; color: var(--dark); }
  .card--back .brand__mark { background: var(--dark); width: 24px; height: 24px; }

  .person { position: absolute; left: 23px; top: 168px; }
  .person__name { font-size: 25px; font-weight: 500; color: var(--teal); letter-spacing: -0.01em; }
  .person__role { font-size: 15px; font-weight: 500; color: var(--ink); margin-top: 8px; }

  .contacts { position: absolute; left: 23px; top: 255px; list-style: none; }
  .contacts li {
    display: flex; align-items: center; gap: 11px;
    height: 23.3px; font-size: 18px; color: var(--teal);
  }
  .contacts svg, .contacts .icon-square { width: 17px; height: 17px; flex: none; }
  .icon-square { display: inline-block; background: var(--teal); border-radius: 2px; width: 15px !important; height: 15px !important; margin: 0 1px; }

  .faint-name {
    position: absolute; right: 22px; top: 285px;
    font-family: "Montserrat", Arial, sans-serif; font-weight: 500;
    font-size: 44px; letter-spacing: 0.06em; text-transform: uppercase;
    color: var(--faint);
  }
  .band { position: absolute; left: 0; right: 0; bottom: 0; height: 16px; background: var(--teal); }

  .services {
    position: absolute; top: 294px; list-style: none;
    font-size: 14.5px; color: var(--dark); text-transform: uppercase; line-height: 1.1;
  }
  .services--left { left: 93px; }
  .services--right { left: 357px; }
  .services li { position: relative; padding-left: 21px; margin-bottom: 6px; }
  .services li::before {
    content: ""; position: absolute; left: 0; top: 3px;
    width: 6px; height: 6px; background: var(--dark);
  }
  .services small { display: block; font-size: 11px; }
</style>
</head>
<body>
  <section class="card card--front">
    <div class="brand"><span class="brand__mark"></span><span>Tidewell<br>Electrical<br>Solutions</span></div>

    <div class="person">
      <h1 class="person__name">MARTIN K. ODUYA</h1>
      <p class="person__role">PROJECT MANAGER</p>
    </div>

    <ul class="contacts">
      <li>
        <svg viewBox="0 0 24 24" aria-hidden="true"><path fill="var(--teal)" d="M6.6 10.8c1.4 2.8 3.8 5.1 6.6 6.6l2.2-2.2c.3-.3.7-.4 1-.2 1.1.4 2.3.6 3.6.6.6 0 1 .4 1 1V20c0 .6-.4 1-1 1C10.6 21 3 13.4 3 4c0-.6.4-1 1-1h3.5c.6 0 1 .4 1 1 0 1.3.2 2.5.6 3.6.1.3 0 .7-.2 1z"/></svg>
        (441) 555-0187
      </li>
      <li><span class="icon-square"></span>@twlelectricalsolutions</li>
      <li><span class="icon-square"></span>@twlelectricalsolutions</li>
      <li>
        <svg viewBox="0 0 24 24" aria-hidden="true"><path fill="var(--teal)" d="M2 5h20v14H2z"/><path fill="none" stroke="#fff" stroke-width="1.6" d="M2.5 5.8 12 13l9.5-7.2"/></svg>
        twlelectricalsoultions@mailpost-demo.com
      </li>
    </ul>

    <div class="faint-name" aria-hidden="true">Tidewell</div>
    <div class="band"></div>
  </section>

  <section class="card card--back">
    <div class="brand"><span class="brand__mark"></span><span>Tidewell<br>Electrical<br>Solutions</span></div>

    <ul class="services services--left">
      <li>LED Lighting &amp; Automation</li>
      <li>Electrical Construction<br>&amp; Maintenance</li>
    </ul>
    <ul class="services services--right">
      <li>Data &amp; Communication</li>
      <li>Life Safety Systems<small>(Fire Alarm / Security)</small></li>
    </ul>
  </section>
</body>
</html>
```